Torque Wizard Works LLC

We Need a business card design for a boat/car mechanic. Our thinking is to have Maybe a car on left side of card, boat on the right side of card and diagnostic computer in the middle and a cool creative way to connect all three together. We are also open to other ideas as well!
Would like for back of business card to have the contact info on it “Dorian Kelleway, text is best as the contact method 803-555-0192”

```html
<!DOCTYPE html>
<html lang="en">
<head>
<meta charset="utf-8">
<title>Torque Wizard Works LLC – Business Card</title>
<link rel="stylesheet" href="https://fonts.googleapis.com/css2?family=Michroma&family=Exo+2:wght@400;600&display=swap">
<style>
  :root {
    --page-bg: #2b2e33;
    --card-black: #121212;
    --brand-red: #e0262b;
    --text-white: #f4f4f4;
    --text-soft: #cfcfcf;
    --sea-blue: #3f6f86;
    --boat-white: #d9dcdc;
    --screen-blue: #2d6fb8;
    --studio-white: #f1f1f1;
    --car-white: #e7e7e7;
    --car-gold: #c98a2a;
  }
  * { box-sizing: border-box; margin: 0; padding: 0; }
  html, body {
    width: 1200px; height: 985px; overflow: hidden;
    background: var(--page-bg);
  }
  .sheet {
    width: 1200px; height: 985px;
    display: flex; flex-direction: column; align-items: center;
    justify-content: center; gap: 65px;
  }
  .card {
    position: relative;
    width: 700px; height: 400px;
    border-radius: 22px;
    background: var(--card-black);
    overflow: hidden;
    box-shadow: 0 14px 30px rgba(0,0,0,.45);
  }

  /* Front */
  .collage { position: absolute; inset: 0; width: 700px; height: 400px; }
  .brand {
    position: absolute;
    display: flex; align-items: center; gap: 22px;
  }
  .card-front .brand { left: 385px; top: 110px; }
  .brand-mark {
    width: 66px; height: 66px; border-radius: 50%;
    background: var(--brand-red);
    flex: none;
  }
  .brand-divider {
    width: 2px; align-self: stretch;
    background: var(--brand-red);
  }
  .brand-name {
    font-family: "Michroma", sans-serif;
    color: var(--text-white);
    font-size: 24px; line-height: 1.28;
    text-transform: uppercase;
    letter-spacing: 1px;
  }

  /* Back */
  .card-back .brand { left: 150px; top: 70px; }
  .card-back .brand-mark { width: 90px; height: 90px; }
  .contact {
    position: absolute; left: 150px; top: 240px;
    font-family: "Exo 2", sans-serif;
  }
  .contact-name {
    font-family: "Michroma", sans-serif;
    color: var(--text-white);
    font-size: 19px; letter-spacing: 1.5px;
    text-transform: uppercase;
  }
  .contact-rule {
    width: 170px; height: 2px; margin: 12px 0 10px;
    background: var(--brand-red);
  }
  .contact-line {
    color: var(--text-soft); font-size: 17px; letter-spacing: .4px;
    display: flex; align-items: center; gap: 10px;
  }
  .contact-phone {
    color: var(--brand-red); font-weight: 600; letter-spacing: 1px;
  }
</style>
</head>
<body>
<main class="sheet">

  <section class="card card-front" aria-label="Business card front">
    <svg class="collage" viewBox="0 0 700 400" aria-hidden="false">
      <defs>
        <clipPath id="photo-zone">
          <polygon points="0,0 215,0 340,400 0,400"/>
        </clipPath>
        <linearGradient id="boat-tone" x1="0" y1="0" x2="1" y2="1">
          <stop offset="0" stop-color="var(--sea-blue)"/>
          <stop offset="1" stop-color="var(--boat-white)"/>
        </linearGradient>
        <linearGradient id="computer-tone" x1="0" y1="0" x2="1" y2="0">
          <stop offset="0" stop-color="var(--studio-white)"/>
          <stop offset="1" stop-color="var(--screen-blue)"/>
        </linearGradient>
        <linearGradient id="car-tone" x1="0" y1="0" x2="1" y2="1">
          <stop offset="0" stop-color="var(--car-white)"/>
          <stop offset="1" stop-color="var(--car-gold)"/>
        </linearGradient>
      </defs>
      <g clip-path="url(#photo-zone)">
        <rect role="img" aria-label="Photo of a white motor boat on blue water" x="0" y="0" width="340" height="135" fill="url(#boat-tone)"/>
        <rect role="img" aria-label="Photo of a diagnostic desktop computer with monitor and keyboard" x="0" y="135" width="340" height="130" fill="url(#computer-tone)"/>
        <rect role="img" aria-label="Photo of a white sports car with gold wheels" x="0" y="265" width="340" height="135" fill="url(#car-tone)"/>
      </g>
      <line x1="215" y1="0" x2="340" y2="400" stroke="var(--brand-red)" stroke-width="7"/>
    </svg>
    <div class="brand">
      <span class="brand-mark"></span>
      <span class="brand-divider"></span>
      <p class="brand-name">Torque<br>Wizard<br>Works LLC</p>
    </div>
  </section>

  <section class="card card-back" aria-label="Business card back">
    <div class="brand">
      <span class="brand-mark"></span>
      <span class="brand-divider"></span>
      <p class="brand-name">Torque<br>Wizard<br>Works LLC</p>
    </div>
    <div class="contact">
      <p class="contact-name">Dorian Kelleway</p>
      <div class="contact-rule"></div>
      <p class="contact-line">text is best as the contact method <span class="contact-phone">803-555-0192</span></p>
    </div>
  </section>

</main>
</body>
</html>
```